Book and Ebook Cover for my Upcoming Book

About the Book
------------------
I need a book, ebook and if possible audio cover design for my upcoming book - Lanterns & Tides. This is my first book and really looking for a great book cover. The book is about my story, living with Mental Health and how to reclaim control of your life.

Pressmarble
-----------
I am using pressmarble.example to self-publish my book so in case of any design-related questions you can just search info on their website.

I have an initial theme I am thinking for the design book cover which I have attached. You can use this as a starting point.

Idea for the theme
---------------------
I am thinking about a phoenix to represent rising from the ashes and rebirth. The phoenix motif will be continued throughout the interior pages of the book. I'd like the cover of the book to be minimal, white with gold lettering, and maybe incorporating wings? feel free to play around with the idea and up for suggestions.

If you can think of something along these lines and make it a lot better that would be great.

What I need
---------------
The book is complete and is Trim size is 6.14 x 9.21” (234 x 156mm). I would need-
1. Book Cover
2. Back & Spine Design
3. Source File
4. Ebook Cover
5. Need multiple revisions to get the best possible outcome
6. My name and book title should also on the front cover
7. The book title should be bigger size than the subtitle

If you can give me Audiobook cover, I would love that as well and can pay extra for it if needed.

I love this for the interior phoenix motif:
https://artbazaarhub.example/VelloStudioWorks/7720418-Painted-Firebird-Graphic-Pack#fullscreen

The only other actual book cover I found online that remotely relates to what I am looking for is this -
https://www.searchloop.example/url?sa=i&url=https%3A%2F%2Fshotgallery.example%2Fkorvath&psig=BxQmTr7LK2pNvW4ZsYeHd83QaPLJ&ust=1598415525610000&source=images&cd=vfe&ved=1HXdkRmQBvubDGrTLkxbWsTqYhpTGEgcDHRRRRRHdBBBBBBCE

Target Market(s)

Personal Development
Mental health

Requirements
Must have
• 1. Book Cover
2. Back & Spine Design
3. Source File
4. Ebook Cover
Nice to have
• Audiobook cover as I eventually will be releasing the audio version of the book

```html
<!DOCTYPE html>
<html lang="en">
<head>
<meta charset="utf-8">
<title>Lanterns &amp; Tides — Book Cover</title>
<link rel="stylesheet" href="https://fonts.googleapis.com/css2?family=Bebas+Neue&family=Poppins:wght@600;700&display=swap">
<style>
  :root {
    --backdrop: #e4e4e5;
    --cover-black: #050505;
    --paper: #ffffff;
    --ink: #1a1a1a;
    --title-white: #ffffff;
    --tide-teal: #3fb8c4;
    --tide-deep: #0f4f58;
    --flame-gold: #f5a533;
    --flame-ember: #c24a12;
  }
  * { margin: 0; padding: 0; box-sizing: border-box; }
  html, body {
    width: 847px; height: 1200px; overflow: hidden;
    background: var(--backdrop);
  }
  .cover {
    position: absolute; left: 70px; top: 69px;
    width: 708px; height: 1062px;
    background: var(--cover-black);
    overflow: hidden;
  }
  .cover-art {
    position: absolute; left: 0; top: 262px;
    width: 708px; height: 692px;
  }
  .title {
    position: absolute; left: 0; right: 0; top: 36px;
    font-family: "Bebas Neue", "Oswald", sans-serif;
    font-weight: 400;
    color: var(--title-white);
    text-align: center;
    font-size: 141px;
    line-height: 122px;
    letter-spacing: 16px;
  }
  .title span { display: block; padding-left: 16px; }
  .subtitle {
    position: absolute; left: 0; right: 0; top: 300px;
    font-family: "Bebas Neue", "Oswald", sans-serif;
    color: var(--title-white);
    text-align: center;
    font-size: 37px;
    line-height: 35px;
    letter-spacing: 0.3px;
  }
  .footer-rule {
    position: absolute; left: 0; top: 953px;
    width: 677px; height: 8px;
    background: var(--cover-black);
  }
  .footer-band {
    position: absolute; left: 0; top: 963px;
    width: 708px; height: 99px;
    background: var(--paper);
  }
  .publisher-tab {
    position: absolute; left: 43px; top: 908px;
    width: 178px; height: 60px;
    background: var(--paper);
    border-radius: 8px 8px 0 0;
  }
  .publisher-name {
    position: absolute; left: 43px; top: 1005px;
    width: 178px;
    font-family: "Poppins", sans-serif;
    font-weight: 700;
    font-size: 18px;
    line-height: 1;
    letter-spacing: 14px;
    padding-left: 14px;
    text-align: center;
    color: var(--ink);
  }
  .author {
    position: absolute; left: 305px; top: 988px;
    font-family: "Poppins", sans-serif;
    font-weight: 600;
    font-size: 40px;
    line-height: 1;
    color: var(--ink);
  }
</style>
</head>
<body>
  <main class="cover">
    <svg class="cover-art" viewBox="0 0 708 692" role="img"
         aria-label="Illustration of a phoenix rising with one wing of splashing teal water and one wing of golden flame">
      <defs>
        <linearGradient id="elementSweep" x1="0" y1="0" x2="1" y2="0">
          <stop offset="0" stop-color="var(--tide-deep)"/>
          <stop offset="0.3" stop-color="var(--tide-teal)"/>
          <stop offset="0.52" stop-color="#e9f1ee"/>
          <stop offset="0.7" stop-color="var(--flame-gold)"/>
          <stop offset="1" stop-color="var(--flame-ember)"/>
        </linearGradient>
        <linearGradient id="topFade" x1="0" y1="0" x2="0" y2="1">
          <stop offset="0" stop-color="#050505" stop-opacity="1"/>
          <stop offset="0.45" stop-color="#050505" stop-opacity="0.35"/>
          <stop offset="1" stop-color="#050505" stop-opacity="0"/>
        </linearGradient>
      </defs>
      <rect width="708" height="692" fill="url(#elementSweep)"/>
      <rect width="708" height="692" fill="url(#topFade)"/>
    </svg>

    <h1 class="title"><span>LANTERNS</span><span>&amp; TIDES</span></h1>
    <p class="subtitle">FIND YOUR<br>QUIET STRENGTH, RESHAPE<br>YOUR DAYS AND GENTLY<br>CARRY YOUR LIGHT</p>

    <div class="footer-rule"></div>
    <div class="footer-band"></div>
    <div class="publisher-tab"></div>
    <p class="publisher-name">TARROW</p>
    <p class="author">by Selvi Arun</p>
  </main>
</body>
</html>
```